Inner pages for Velbrin Tune

***PLEASE NOTE***
Please do not vie for this project if you were not invited. This project was meant for a particular designer but was erroneously created as a contest. Thank you.
**********

I need HTML/CSS files for the design that was done for the front page attached.
I also need designs and HTML for these inner pages to match the template:
http://www.velbrin-tune.net/documentation/how-the-plugin-works.html
http://www.velbrin-tune.net/support/knowlegebase.html
http://www.velbrin-tune.net/support/knowlegebase.html?View=entry&EntryID=9
http://www.velbrin-tune.net/subscribe/new.html
http://www.velbrin-tune.net/downloads.html

For the downloads page (http://www.velbrin-tune.net/downloads.html), I'm going to be providing download links to files for four different platforms. (That's the plan anyway) So that row that has the Download/Subscribe buttons would be repeated 4 times, one for each platform (That's shown on the front page)

```html
<!DOCTYPE html>
<html lang="en">
<head>
<meta charset="utf-8">
<title>Subscribe — Velbrin Tune</title>
<link href="https://fonts.googleapis.com/css2?family=Lato:wght@300;400;700;900&display=swap" rel="stylesheet">
<style>
:root{
  --green:#6fb43f;
  --dark:#5d5d5d;
  --footer:#585858;
  --text:#444;
  --muted:#777;
  --field:#f2f2f2;
  --page:#f7f7f7;
  --chip:#c9ced6;
}
*{box-sizing:border-box;margin:0;padding:0}
html,body{width:804px;height:1200px;overflow:hidden}
body{font-family:'Lato',sans-serif;color:var(--text);background:var(--page);position:relative}
.abs{position:absolute}
.site-header{position:absolute;left:0;top:0;width:804px;height:72px;background:#fafafa}
.brand{left:92px;top:0;height:60px;display:flex;align-items:center;gap:8px;font-weight:900;font-size:21px;color:var(--green)}
.brand .mark{width:14px;height:14px;background:#666}
.main-nav{left:354px;top:1px;display:flex;align-items:center;font-size:10px;color:#555}
.main-nav a{color:#555;text-decoration:none;padding:4px 7px;height:21px;display:flex;align-items:center}
.main-nav .active{border:1px solid var(--green);color:var(--green);padding:4px 11px}
.main-nav .boxed{border:1px solid var(--green)}
.login-btn{left:661px;top:1px;width:50px;height:21px;background:#444;color:#fff;font-size:10px;display:flex;align-items:center;justify-content:center;gap:4px}
.search{left:534px;top:35px;display:flex;height:21px}
.search input{width:118px;border:1px solid #999;font:8px 'Lato',sans-serif;padding:0 5px;background:#fff}
.search button{width:59px;background:#555;color:#fff;border:0;font:700 10px 'Lato',sans-serif}
.hero{left:0;top:72px;width:804px;height:147px;background:radial-gradient(ellipse at center,#8cc65e 0%,#6db03e 70%)}
.hero .crumbs{left:94px;top:14px;font-size:8.5px;color:#fff;font-weight:700}
.hero .rule{left:200px;width:404px;height:1px;background:rgba(255,255,255,.25)}
.hero h1{left:0;top:55px;width:804px;text-align:center;color:#fff;font-weight:900;font-size:29px}
.crumbs-body{left:94px;top:242px;font-size:9px;color:var(--muted)}
.steps{left:92px;top:276px;width:619px;height:76px;background:var(--dark);color:#fff;text-align:center}
.steps p{margin-top:19px;font-size:11px}
.steps ol{list-style:none;display:flex;justify-content:center;gap:28px;margin-top:8px;margin-left:-16px}
.steps li{display:flex;align-items:center;gap:5px;font-size:15px;font-weight:700;color:#aaa}
.steps li.on{color:#fff}
.steps .num{width:16px;height:16px;border-radius:50%;border:1.5px solid #bbb;font-size:9px;display:flex;align-items:center;justify-content:center;font-weight:400}
.steps li.on .num{background:var(--green);border-color:#fff}
.product{left:92px;top:352px;width:620px;height:88px;background:#fff;border:1px solid #eee}
.product h2{position:absolute;left:14px;top:29px;font-size:20px;font-weight:400;color:#333}
.product .mini-brand{position:absolute;right:8px;top:38px;font-weight:900;font-size:15px;color:#222}
h3.section{font-size:15.5px;font-weight:700;color:#444;display:flex;align-items:center;gap:6px}
.icon{width:11px;height:13px}
.row-label{font-size:9.5px;color:#555}
.small-label{font-size:7px;color:#555}
.field{background:var(--field);border:1px solid #ccc;height:22px}
.btn-green{background:var(--green);color:#fff;font-weight:900;font-size:11px;display:flex;align-items:center;justify-content:center}
.sum-dollar{width:24px;height:22px;border:1px solid #ccc;background:var(--field);color:var(--green);font-weight:900;font-size:10px;display:flex;align-items:center;justify-content:center}
.sum-val{width:157px;height:22px;border:1px solid #ccc;background:var(--field);font-size:8px;display:flex;align-items:center;justify-content:center}
.total .sum-dollar,.total .sum-val{border-color:var(--green);color:var(--green)}
.divider{left:92px;top:638px;width:619px;height:1px;background:#e2e2e2}
.select{display:flex;justify-content:space-between;align-items:center;padding-left:10px;font-size:8px;color:var(--green)}
.select .caret{width:22px;height:100%;border-left:1px solid #ccc;display:flex;align-items:center;justify-content:center}
.radio{width:9px;height:9px;border-radius:50%;border:1px solid #aaa;background:#eee}
.card{width:15px;height:10px;background:var(--chip)}
.method-name{font-size:7px;font-weight:700;color:#555}
.pay-box{left:555px;top:795px;width:156px;height:49px;background:#fff}
.pay-box .inner{position:absolute;left:10px;top:6px;width:138px;height:38px;border:1px solid #ddd;background:#f4f4f4;display:flex;flex-direction:column;align-items:center;justify-content:center;gap:4px}
.pay-box .name{font-weight:700;font-size:11px;color:#555}
.subscribe-now{left:92px;top:947px;width:619px;height:34px;background:var(--green);color:#fff;font-weight:900;font-size:15.5px;padding-left:12px;display:flex;align-items:center}
.site-footer{left:0;top:1008px;width:804px;height:192px;background:var(--footer);color:#ccc}
.foot-links{position:absolute;left:92px;top:24px;width:619px;display:flex;justify-content:space-between;font-size:8px}
.foot-rule{position:absolute;left:0;top:50px;width:804px;height:1px;background:linear-gradient(90deg,transparent,#777,transparent)}
.copyright{position:absolute;left:92px;top:87px;font-size:8px}
.foot-brand{position:absolute;left:300px;top:101px;width:208px;text-align:center;font-weight:900;font-size:17px;color:#9a9a9a}
.foot-brand .mark{display:block;width:14px;height:14px;background:#9a9a9a;margin:0 auto 6px}
.legal{position:absolute;right:93px;top:87px;display:flex;gap:10px;font-size:8px}
.license{position:absolute;left:92px;top:155px;font-size:8px;color:var(--green)}
.social{position:absolute;left:645px;top:156px;display:flex;gap:6px}
.social span{width:17px;height:17px;border-radius:3px;background:#7a7a7a}
</style>
</head>
<body>

<header class="site-header">
  <div class="abs brand"><span class="mark"></span>Velbrin Tune</div>
  <nav class="abs main-nav">
    <a class="active">Home</a><a>Documentation</a><a>Support</a><a>Downloads</a><a class="boxed">Subscribe</a>
  </nav>
  <div class="abs login-btn">
    <svg width="9" height="9" viewBox="0 0 10 10"><circle cx="5" cy="3" r="2.2" fill="none" stroke="#fff"/><path d="M1 9.5c0-2.5 8-2.5 8 0" fill="none" stroke="#fff"/></svg>Login
  </div>
  <form class="abs search"><input placeholder="Enter Your Keyword"><button type="button">Search</button></form>
</header>

<section class="abs hero">
  <div class="abs crumbs">You are here:Home &nbsp;/&nbsp; Documentation &nbsp;/&nbsp; How the plugin works</div>
  <div class="abs rule" style="top:50px"></div>
  <h1 class="abs">SUBSCRIBE</h1>
  <div class="abs rule" style="top:97px"></div>
</section>

<div class="abs crumbs-body">You are here:Home/ Subscribe</div>

<section class="abs steps">
  <p>Subscribing is easy; just three simple steps to follow</p>
  <ol>
    <li class="on"><span class="num">1</span>Sign Up</li>
    <li><span class="num">2</span>Pay</li>
    <li><span class="num">3</span>Start Using</li>
  </ol>
</section>

<section class="abs product">
  <h2>VELBRINTUNEPRO</h2>
  <div class="mini-brand">Velbrin Tune</div>
</section>

<h3 class="abs section" style="left:92px;top:464px">
  <svg class="icon" viewBox="0 0 12 14"><path d="M5 1h6v12H5M1 7h7M5 4l3 3-3 3" fill="none" stroke="var(--green)" stroke-width="1.3"/></svg>Login
</h3>
<div class="abs row-label" style="left:93px;top:511px">User Name</div>
<div class="abs field" style="left:148px;top:506px;width:246px"></div>
<div class="abs row-label" style="left:98px;top:546px">Password</div>
<div class="abs field" style="left:147px;top:540px;width:246px"></div>
<div class="abs btn-green" style="left:148px;top:574px;width:60px;height:21px">LOGIN</div>
<div class="abs small-label" style="left:213px;top:581px;font-size:7.5px;color:#666">or fill in the form below to create a new account</div>

<h3 class="abs section" style="left:455px;top:461px">
  <svg class="icon" viewBox="0 0 12 14"><rect x="1" y="1" width="10" height="12" fill="none" stroke="var(--green)" stroke-width="1.3"/><path d="M3 5h6M3 8h6M3 11h4" stroke="var(--green)"/></svg>Summary
</h3>
<div class="abs small-label" style="left:456px;top:500px">Regular price</div>
<div class="abs" style="left:520px;top:493px;display:flex"><div class="sum-dollar">$</div><div class="sum-val">5.00</div></div>
<div class="abs small-label" style="left:456px;top:532px">Discount</div>
<div class="abs" style="left:520px;top:524px;display:flex"><div class="sum-dollar">$</div><div class="sum-val">0.00</div></div>
<div class="abs small-label" style="left:456px;top:564px">Taxes</div>
<div class="abs" style="left:520px;top:556px;display:flex"><div class="sum-dollar">$</div><div class="sum-val">0.00</div></div>
<div class="abs small-label" style="left:456px;top:595px;color:var(--green)">Total charge</div>
<div class="abs total" style="left:520px;top:587px;display:flex"><div class="sum-dollar">$</div><div class="sum-val">5.00</div></div>

<div class="abs divider"></div>

<h3 class="abs section" style="left:92px;top:667px">Information for your new account on our site</h3>
<div class="abs small-label" style="left:92px;top:706px">Username</div>
<div class="abs field" style="left:202px;top:698px;width:204px"></div>
<div class="abs small-label" style="left:92px;top:740px">Password</div>
<div class="abs field" style="left:202px;top:730px;width:204px"></div>
<div class="abs small-label" style="left:92px;top:773px">Retype Password</div>
<div class="abs field" style="left:202px;top:762px;width:204px"></div>
<div class="abs small-label" style="left:92px;top:807px">Full name (in latin characters)</div>
<div class="abs field" style="left:202px;top:793px;width:204px"></div>
<div class="abs small-label" style="left:92px;top:837px">Email</div>
<div class="abs field" style="left:202px;top:825px;width:204px"></div>
<div class="abs small-label" style="left:92px;top:866px">Email (repeat it)</div>
<div class="abs field" style="left:202px;top:856px;width:204px"></div>
<div class="abs small-label" style="left:92px;top:896px">I agree to the Terms of Service</div>
<div class="abs field select" style="left:202px;top:887px;width:204px">NO<span class="caret"><svg width="7" height="4"><path d="M0 0h7L3.5 4z" fill="#444"/></svg></span></div>

<h3 class="abs section" style="left:455px;top:667px">
  <svg width="15" height="15" viewBox="0 0 14 14"><circle cx="2" cy="12" r="1.8" fill="var(--green)"/><path d="M1 6a7 7 0 0 1 7 7M1 1a12 12 0 0 1 12 12" fill="none" stroke="var(--green)" stroke-width="2"/></svg>Subscribe
</h3>
<div class="abs small-label" style="left:477px;top:706px">Coupon code</div>
<div class="abs field" style="left:541px;top:698px;width:162px"></div>
<div class="abs small-label" style="left:476px;top:743px;color:var(--green)">Payment method</div>
<div class="abs radio" style="left:535px;top:742px"></div>
<div class="abs" style="left:548px;top:737px;display:flex;align-items:center;gap:3px">
  <span style="width:18px;height:18px;border-radius:50%;background:#aab2bd"></span>
  <span class="method-name">Checkra</span>
</div>
<div class="abs" style="left:606px;top:741px;display:flex;gap:3px">
  <span class="card"></span><span class="card"></span><span class="card"></span><span class="card"></span><span class="card"></span><span class="card"></span>
</div>
<div class="abs" style="left:606px;top:755px;display:flex;gap:3px"><span class="card"></span><span class="card"></span></div>
<div class="abs radio" style="left:538px;top:811px"></div>
<div class="abs pay-box">
  <div class="inner">
    <span class="name">Payvora</span>
    <span style="display:flex;gap:3px"><span class="card"></span><span class="card"></span><span class="card"></span><span class="card"></span><span class="card"></span></span>
  </div>
</div>

<div class="abs subscribe-now">SUBSCRIBE NOW!</div>

<footer class="abs site-footer">
  <nav class="foot-links">
    <span>Lumora CMS</span><span>|</span><span>Gridwell Kit</span><span>|</span><span>Stylo Website</span><span>|</span><span>HTML5</span><span>|</span><span>Revealo Website</span><span>|</span><span>Glyphset</span><span>|</span><span>Downloads</span>
  </nav>
  <div class="foot-rule"></div>
  <div class="copyright">Copyright © 2013 Velbrin Tune, All rights reserved.</div>
  <div class="foot-brand"><span class="mark"></span>Velbrin Tune</div>
  <div class="legal"><span>Terms of Use</span><span>Privacy Policy</span><span>Refund Policy</span><span>Contact Us</span></div>
  <div class="license">Velbrin Tune is released under the Open Commons License.</div>
  <div class="social"><span></span><span></span><span></span></div>
</footer>

</body>
</html>
```